Design an Office Mural for Electrical Engineering Company

We have a blank wall in our commercial office space that we would love to decorate with custom wallpaper. For this purpose, we are seeking a design to have printed as wallpaper and hung on the wall.

The design should include typography with our slogan "elevate your expectations". It is important that the design uses orange, charcoal and dark blue but other colours can also be incorporated. We want this graphic to appeal to our workforce of young, fun and intelligent men. You may like to include elements of engineering, electrical and automation in your graphic.

I have attached our logo for reference. You can choose whether or not to incorporate design elements from the logo but please DO NOT cut and paste the logo onto your design. I have attached examples of other murals that we like. Please use these as a reference for the style of your work.

The wall dimensions are 2m wide by 2.6m tall. Unfortunately we don't have a photo of the wall as it is under construction.

Target Market(s)

Young - Middle Aged Men, Tradesmen, Business People, Industrial Clients

Industry/Entity Type

Electrical engineering, factory automation, industrial maintenance

Colors
0054AA
0677BA
7BADD7
CADEEF
E8F1F8
F0912C
F2A743
F7CA91
FBE8D2
FDF5EE

Requirements
Must have
• Company colours (orange and charcoal), slogan "elevate your expectations"
Nice to have
• Hand lettering and illustration
Should not have
• The logo copy and pasted on the design. Stock images or any photographs.

```html
<!DOCTYPE html>
<html lang="en">
<head>
<meta charset="utf-8">
<title>Elevate Your Expectations – Office Mural</title>
<link rel="stylesheet" href="https://fonts.googleapis.com/css2?family=Saira+Condensed:wght@700&family=Saira+Semi+Condensed:wght@500;700&family=Exo+2:wght@700&family=Lato:wght@700&display=swap">
<style>
  :root {
    --canvas-bg: #e8e9eb;
    --charcoal: #333e4a;
    --orange: #f2a743;
    --orange-deep: #f0912c;
    --sky: #5aaee6;
    --white: #ffffff;
    --gear-tone: #3c4957;
  }
  html, body {
    margin: 0;
    padding: 0;
    width: 1200px;
    height: 800px;
    overflow: hidden;
    background: var(--canvas-bg);
  }
  .canvas {
    position: relative;
    width: 1200px;
    height: 800px;
    display: flex;
    align-items: center;
    justify-content: center;
  }
  .mural {
    display: block;
    width: 554px;
    height: 720px;
  }
  .mural__bg { fill: var(--charcoal); }
  .brand__mark { fill: var(--orange-deep); }
  .brand__name {
    font-family: "Lato", sans-serif;
    font-weight: 700;
    font-size: 13px;
    fill: var(--white);
  }
  .slogan__elevate {
    font-family: "Saira Condensed", sans-serif;
    font-weight: 700;
    font-size: 100px;
    fill: var(--white);
  }
  .slogan__your {
    font-family: "Saira Semi Condensed", sans-serif;
    font-size: 100px;
  }
  .slogan__your--outline {
    font-weight: 500;
    fill: none;
    stroke: var(--white);
    stroke-width: 1;
  }
  .slogan__your--faint { stroke-opacity: 0.3; }
  .slogan__your--solid {
    font-weight: 700;
    fill: var(--orange);
  }
  .slogan__expectations {
    font-family: "Exo 2", sans-serif;
    font-weight: 700;
    font-size: 22px;
    fill: var(--sky);
  }
</style>
</head>
<body>
<main class="canvas">
  <svg class="mural" viewBox="0 0 488 634" xmlns="http://www.w3.org/2000/svg">
    <defs>
      <linearGradient id="gear-band-fill" x1="0" y1="0" x2="0" y2="1">
        <stop offset="0" stop-color="#333e4a"/>
        <stop offset="1" stop-color="#3c4957"/>
      </linearGradient>
    </defs>

    <rect class="mural__bg" x="0" y="0" width="488" height="634"/>

    <g class="brand">
      <circle class="brand__mark" cx="244" cy="66" r="22"/>
      <text class="brand__name" x="244" y="128" text-anchor="middle">High Reach</text>
      <text class="brand__name" x="244" y="144" text-anchor="middle">Electrical</text>
    </g>

    <g class="slogan">
      <text class="slogan__elevate" transform="translate(72 159) rotate(90)" x="0" y="0"
            textLength="367" lengthAdjust="spacingAndGlyphs">ELEVATE</text>

      <text class="slogan__your slogan__your--outline slogan__your--faint" x="174" y="232"
            textLength="241" lengthAdjust="spacingAndGlyphs">YOUR</text>
      <text class="slogan__your slogan__your--outline" x="174" y="317"
            textLength="241" lengthAdjust="spacingAndGlyphs">YOUR</text>
      <text class="slogan__your slogan__your--outline" x="174" y="402"
            textLength="241" lengthAdjust="spacingAndGlyphs">YOUR</text>
      <text class="slogan__your slogan__your--solid" x="174" y="487"
            textLength="241" lengthAdjust="spacingAndGlyphs">YOUR</text>

      <text class="slogan__expectations" x="177" y="524"
            textLength="240" lengthAdjust="spacing">EXPECTATIONS</text>
    </g>

    <rect class="gear-band" x="0" y="530" width="488" height="104" fill="url(#gear-band-fill)"
          role="img" aria-label="Faint line pattern of interlocking gears along the bottom edge"/>
  </svg>
</main>
</body>
</html>
```